Flyer-Design für Konzertflyer gemischter Chor
Zielgruppe
Wir, die Klangfreunde Wellbach sind ein gemischter Chor aus der Schweiz. Für unser nächstes Konzert mit dem Titel ' Lieder zum Träumen' brauchen wir einen Flyer der auf den Anlass Aufmerksam macht.
Näheres zum Chor auf unserer Website www.klangfreunde-wellbach.ch.
Aufgabenstellung
Mit dem Titel sind nicht nur Lieder zum verlieben gemeint sondern auch Songs in die man sich verlieben kann oder die einem an etwas schönes Erinnern. Wir denken da an ein stimmungsvolles Design mit nicht nur roten Herzen.
Programmausschnitt: Winds across the silver bay , Harlan Moody / Lanterns in the rain / Kima Soro / Walk beside the quiet river tonight, Garth Wells / Paper boats at dusk, Russ Tanner / Tidal hymn, Trevor Halloway / Brightwater, Harbor lane tales / Bells over meadows , Cedar hall
Format: A5 hochkant.
Text: "Lieder zum Träumen" Konzert Klangfreunde Wellbach.
Samstag 19. November 17.00 Uhr, Uerikon/Stäfa, Singsaal Lindenhain
Sonntag 20. November 17.00Uhr, Uetikon am See, Kornblumsaal
Eintritt frei Kollekte
www.klangfreunde-wellbach.ch

```html
<!DOCTYPE html>
<html lang="de">
<head>
<meta charset="utf-8">
<title>Lieder zum Träumen – Klangfreunde Wellbach</title>
<link href="https://fonts.googleapis.com/css2?family=EB+Garamond:wght@700&family=Barlow+Condensed:wght@300;400;600&family=Pinyon+Script&display=swap" rel="stylesheet">
<style>
  :root {
    --ink: #141010;
    --cream: #fff6c8;
    --sun: #ffd24a;
    --orange: #f7a03c;
    --coral: #f46a5a;
    --rose: #ef5f86;
    --violet: #e28ad8;
  }
  html, body {
    margin: 0;
    padding: 0;
    width: 846px;
    height: 1200px;
    overflow: hidden;
  }
  .flyer {
    position: relative;
    width: 846px;
    height: 1200px;
    overflow: hidden;
    color: var(--ink);
    font-family: "Barlow Condensed", "Arial Narrow", sans-serif;
  }
  .flyer__photo {
    position: absolute;
    inset: 0;
    background:
      radial-gradient(ellipse 420px 300px at 120px 60px, var(--cream) 0%, rgba(255,246,200,0) 100%),
      radial-gradient(ellipse 520px 420px at 300px 420px, rgba(255,214,120,0.9) 0%, rgba(255,214,120,0) 100%),
      radial-gradient(ellipse 420px 380px at 760px 250px, rgba(247,140,60,0.8) 0%, rgba(247,140,60,0) 100%),
      radial-gradient(ellipse 500px 380px at 560px 880px, rgba(240,80,80,0.75) 0%, rgba(240,80,80,0) 100%),
      radial-gradient(ellipse 380px 420px at 840px 1140px, rgba(226,138,216,0.9) 0%, rgba(226,138,216,0) 100%),
      linear-gradient(170deg, var(--sun) 0%, var(--orange) 40%, var(--coral) 72%, var(--rose) 100%);
  }
  .header {
    position: absolute;
    top: 60px;
    left: 0;
    width: 100%;
    text-align: center;
  }
  .header__choir {
    margin: 0;
    font-family: "EB Garamond", Georgia, serif;
    font-weight: 700;
    font-size: 43px;
    line-height: 1;
    letter-spacing: 0.5px;
    text-transform: uppercase;
  }
  .header__presents {
    margin: 6px 0 0;
    font-weight: 300;
    font-size: 25px;
    line-height: 1;
    text-transform: uppercase;
  }
  .programme {
    margin: 22px auto 0;
    width: 800px;
    font-weight: 300;
    font-size: 17.5px;
    line-height: 24px;
  }
  .title {
    position: absolute;
    left: 10px;
    top: 370px;
    margin: 0;
    font-family: "Pinyon Script", cursive;
    font-weight: 400;
    line-height: 0.8;
    color: var(--ink);
  }
  .title span { display: block; }
  .title__one { font-size: 170px; padding-left: 40px; }
  .title__two { font-size: 130px; padding-left: 0; }
  .title__three { font-size: 140px; padding-left: 30px; }
  .dates {
    position: absolute;
    left: 45px;
    top: 858px;
  }
  .event { margin-bottom: 30px; }
  .event__day,
  .event__time {
    display: block;
    font-weight: 600;
    font-size: 31px;
    line-height: 33px;
  }
  .event__place {
    display: block;
    font-weight: 300;
    font-size: 31px;
    line-height: 34px;
  }
  .entry {
    position: absolute;
    left: 45px;
    top: 1124px;
    margin: 0;
    font-weight: 600;
    font-size: 31px;
    line-height: 1;
  }
  .more-info {
    position: absolute;
    right: 44px;
    top: 1136px;
    margin: 0;
    font-weight: 600;
    font-size: 17px;
    line-height: 1;
  }
</style>
</head>
<body>
<main class="flyer">
  <div class="flyer__photo" role="img" aria-label="Warm getöntes Foto einer lächelnden Sängerin mit der Hand am Gesicht, in Gelb-, Orange- und Rosatönen"></div>

  <header class="header">
    <h1 class="header__choir">Klangfreunde Wellbach</h1>
    <p class="header__presents">Präsentieren live:</p>
    <p class="programme">
      Winds across the silver bay, Harlan Moody / Walk beside the quiet river tonight, Garth Wells / Paper boats at dusk, Russ Tanner /<br>
      Tidal hymn, Trevor Halloway / Brightwater, Harbor lane tales / Bells over meadows , Cedar hall ...
    </p>
  </header>

  <h2 class="title">
    <span class="title__one">Lieder</span>
    <span class="title__two">zum</span>
    <span class="title__three">Träumen</span>
  </h2>

  <section class="dates">
    <div class="event">
      <span class="event__day">Samstag, 19. November 2016</span>
      <span class="event__time">17.00 Uhr</span>
      <span class="event__place">Uerikon/Stäfa, Singsaal Lindenhain</span>
    </div>
    <div class="event">
      <span class="event__day">Sonntag, 20. November 2016</span>
      <span class="event__time">17.00Uhr,</span>
      <span class="event__place">Uetikon am See, Kornblumsaal</span>
    </div>
  </section>

  <p class="entry">Eintritt frei Kollekte</p>
  <p class="more-info">Weitere Infos unter: www.klangfreunde-wellbach.ch</p>
</main>
</body>
</html>
```